Digital Marketing company needs business cards

We are a digital marketing company providing SEO, Bidlane and Web Development services in Australia and New Zealand. Colours and icons have to match the current website (kestrelworks.com.au). We'd like to keep the cards simple and clean, using the artwork we have as the background of the slider of the website (the triangles). The card should have horizontal layout.
If we could have our core services on the reverse side that'd be great:
SEO
BidLane
Web Design&Development
Target Market(s)
Medium size to large businesses
Industry/Entity Type
Digital

```html
<!DOCTYPE html>
<html lang="en">
<head>
<meta charset="utf-8">
<title>KestrelWorks Business Cards</title>
<link href="https://fonts.googleapis.com/css2?family=Questrial&family=Didact+Gothic&display=swap" rel="stylesheet">
<style>
  :root {
    --bg: #e9e7e3;
    --card-white: #f4f4f4;
    --blue-deep: #1f6fbf;
    --blue-mid: #3189d3;
    --blue-light: #5aa6e0;
    --ink-dark: #3d3f44;
    --ink-blue: #2a7fcf;
    --white: #ffffff;
  }
  * { box-sizing: border-box; margin: 0; padding: 0; }
  html, body {
    width: 1200px; height: 900px; overflow: hidden;
    background: var(--bg);
    font-family: "Questrial", "Didact Gothic", sans-serif;
  }
  .stage { position: relative; width: 1200px; height: 900px; }
  .card {
    position: absolute; width: 560px; height: 320px;
    background: var(--card-white);
    box-shadow: 0 6px 18px rgba(0,0,0,0.18);
    overflow: hidden;
  }
  .card--back { left: 320px; top: 90px; padding: 8px; }
  .card--front { left: 320px; top: 480px; }

  .triangle-field {
    background: linear-gradient(135deg, var(--blue-deep) 0%, var(--blue-mid) 45%, var(--blue-light) 75%, var(--blue-mid) 100%);
  }
  .card--back .triangle-field {
    width: 100%; height: 100%;
    display: flex; align-items: center; justify-content: center;
  }
  .wordmark {
    display: flex; align-items: center; gap: 12px;
    letter-spacing: 0.5px;
  }
  .wordmark__name { line-height: 1; }
  .wordmark__dot { border-radius: 50%; }
  .card--back .wordmark__name { color: var(--white); font-size: 46px; }
  .card--back .wordmark__dot { width: 44px; height: 44px; border: 5px solid var(--white); }

  .front__top { position: absolute; left: 0; top: 0; width: 100%; height: 112px; }
  .card--front .wordmark { position: absolute; left: 28px; top: 28px; }
  .card--front .wordmark__name { color: var(--ink-dark); font-size: 36px; }
  .card--front .wordmark__dot { width: 34px; height: 34px; border: 4px solid var(--ink-blue); }
  .website {
    position: absolute; right: 28px; top: 88px;
    color: var(--ink-blue); font-size: 14px; letter-spacing: 0.4px;
  }
  .front__band { position: absolute; left: 0; top: 112px; width: 100%; height: 176px; }

  .contacts {
    position: absolute; left: 24px; top: 18px; width: 250px;
    list-style: none;
  }
  .contacts li {
    display: flex; align-items: center; justify-content: flex-end; gap: 10px;
    color: var(--white); font-size: 12.5px; line-height: 1.25;
    text-align: right; min-height: 32px;
  }
  .contacts .icon { flex: none; width: 22px; height: 22px; }
  .person { position: absolute; left: 296px; top: 28px; }
  .person__name { color: var(--white); font-size: 25px; letter-spacing: 0.4px; }
  .person__role {
    color: var(--ink-dark); font-family: "Didact Gothic", sans-serif;
    font-weight: 700; font-size: 14px; margin-top: 6px;
  }
</style>
</head>
<body>
<main class="stage">

  <section class="card card--back" aria-label="Card back">
    <div class="triangle-field" role="img" aria-label="Blue faceted triangle pattern background">
      <div class="wordmark">
        <span class="wordmark__name">kestrelworks</span>
        <span class="wordmark__dot"></span>
      </div>
    </div>
  </section>

  <section class="card card--front" aria-label="Card front">
    <div class="front__top">
      <div class="wordmark">
        <span class="wordmark__name">kestrelworks</span>
        <span class="wordmark__dot"></span>
      </div>
      <p class="website">www.kestrelworks.com.au</p>
    </div>

    <div class="front__band triangle-field" role="img" aria-label="Blue faceted triangle pattern background">
      <ul class="contacts">
        <li>+1 555.210.4400
          <svg class="icon" viewBox="0 0 22 22" fill="none" stroke="#fff" stroke-width="1.6">
            <circle cx="11" cy="11" r="9.5"/>
            <path d="M7.5 6.5c0 5 3 8 8 8l0.5-2-2.2-1-1 1c-1.5-.6-2.7-1.8-3.3-3.3l1-1-1-2.2z" stroke-linejoin="round"/>
          </svg>
        </li>
        <li>+1 555.210.4401
          <svg class="icon" viewBox="0 0 22 22" fill="none" stroke="#fff" stroke-width="1.6">
            <circle cx="11" cy="11" r="9.5"/>
            <rect x="7" y="6.5" width="8" height="9" rx="0.5"/>
            <path d="M8.8 9h4.4M8.8 11h4.4M8.8 13h4.4"/>
          </svg>
        </li>
        <li>maren@kestrelworks.com.au
          <svg class="icon" viewBox="0 0 22 22" fill="none" stroke="#fff" stroke-width="1.6">
            <circle cx="11" cy="11" r="9.5"/>
            <rect x="6" y="7.5" width="10" height="7"/>
            <path d="M6 7.5l5 4 5-4"/>
          </svg>
        </li>
        <li>KestrelWorks, Streetname 123<br>State ZIP code 123456
          <svg class="icon" viewBox="0 0 22 22" fill="none" stroke="#fff" stroke-width="1.6">
            <circle cx="11" cy="11" r="9.5"/>
            <path d="M11 16.5s-3.5-3.8-3.5-6.3a3.5 3.5 0 0 1 7 0c0 2.5-3.5 6.3-3.5 6.3z"/>
            <circle cx="11" cy="10.2" r="1.2"/>
          </svg>
        </li>
      </ul>
      <div class="person">
        <p class="person__name">Maren Holloway</p>
        <p class="person__role">Director</p>
      </div>
    </div>
  </section>

</main>
</body>
</html>
```